wooden jewelry - pearl necklaces

I sell wooden jeweler (rings and pearls) on markets, and so on. I also opened my business as a carpenter. The rings and a combination of wood and metal. The wood is special wood, not very common on Europe. I paint the rings afterwards. You can see some of the pictures on the pictures I uploaded. The pearls are made of the same kind of wood and colored in all kinds of colors. They are then assembled to bracelets. The jewelry is very individual and looks really cool and all kinds of people.

Target Market(s)

Young urban alternative with a sense of individuality

Contact Information for Business Card

Front:

Text:

„Kugelwerk“ (big)
„Malte Oswitz“ (smaler)

Back
„RINGHOLZ
Herstellung von individuellem Holz- und Modeschmuck

Malte Oswitz
Tel: 015239460518
Lindgarbweg 9
83127 Altmühlried

malteoswitz@postfeld.de“

Font styles to use
Sans Serif

Requirements
Nice to have
• Nice to see a camel thorn tree on the background, this is a special wood and some of the rings are made out of this wood.

```html
<!DOCTYPE html>
<html lang="de">
<head>
<meta charset="utf-8">
<title>Kugelwerk – Visitenkarte</title>
<link rel="stylesheet" href="https://fonts.googleapis.com/css2?family=Jost:wght@500;600&family=Source+Sans+3:wght@400;600;700&display=swap">
<style>
  :root {
    --page: #ffffff;
    --card-light: #ffffff;
    --ink: #1e1e1e;
    --panel-dark: #242424;
    --white: #ffffff;
    --wood-deep: #3a2a2c;
    --wood-mid: #6b5a55;
    --ring-steel: #5d6f8a;
    --bead-dark: #231c27;
    --bead-mid: #3a2c35;
    --bead-warm: #4a3a36;
  }
  * { margin: 0; padding: 0; box-sizing: border-box; }
  html, body { width: 1200px; height: 900px; overflow: hidden; background: var(--page); }
  .canvas { position: relative; width: 1200px; height: 900px; }

  .card { position: absolute; border-radius: 14px; overflow: hidden; }

  /* back side */
  .card-back { left: 292px; top: 90px; width: 564px; height: 324px; background: var(--card-light); border: 1px solid #e4e4e4; }
  .holder-name { position: absolute; left: 21px; top: 30px; font-family: "Jost", sans-serif; font-weight: 600; font-size: 21px; letter-spacing: 1.6px; color: var(--ink); }
  .info-band { position: absolute; left: 0; top: 80px; width: 550px; height: 164px; }
  .band-edge { position: absolute; top: 0; height: 100%; background: var(--panel-dark); }
  .band-edge.left { left: 0; width: 22px; }
  .band-edge.right { left: 540px; width: 10px; }
  .contact-panel { position: absolute; left: 27px; top: 0; width: 265px; height: 100%; background: var(--panel-dark); padding: 60px 0 0 34px; font-family: "Source Sans 3", sans-serif; font-size: 13.5px; line-height: 21px; color: var(--white); }
  .product-photo { position: absolute; left: 304px; top: 0; width: 236px; height: 100%;
    background: radial-gradient(ellipse 45% 55% at 48% 40%, var(--ring-steel) 0%, rgba(93,111,138,0) 70%),
                linear-gradient(160deg, var(--wood-mid) 0%, var(--wood-deep) 60%, #2b2022 100%); }
  .brand-name { position: absolute; left: 0; right: 0; top: 70px; text-align: center; color: var(--white);
    font-family: "Source Sans 3", sans-serif; font-weight: 600; font-size: 24px; letter-spacing: 1.4px; line-height: 1; }
  .address { position: absolute; left: 21px; top: 264px; font-family: "Source Sans 3", sans-serif; font-style: normal; font-size: 13.5px; line-height: 19px; color: var(--ink); }

  /* front side */
  .card-front { left: 288px; top: 495px; width: 570px; height: 327px;
    background: radial-gradient(circle at 20% 30%, var(--bead-warm) 0%, rgba(74,58,54,0) 45%),
                radial-gradient(circle at 80% 75%, var(--bead-mid) 0%, rgba(58,44,53,0) 50%),
                var(--bead-dark); }
  .front-text { position: absolute; left: 0; right: 0; text-align: center; color: var(--white); }
  .front-title { top: 96px; font-family: "Jost", sans-serif; font-weight: 600; font-size: 76px; letter-spacing: 2px; line-height: 1; }
  .front-name { top: 180px; font-family: "Source Sans 3", sans-serif; font-weight: 400; font-size: 49px; line-height: 1; }
</style>
</head>
<body>
<main class="canvas">
  <section class="card card-back" aria-label="Rückseite">
    <h2 class="holder-name">MALTE OSWITZ</h2>
    <div class="info-band">
      <div class="band-edge left"></div>
      <div class="contact-panel">
        <p>Tel: 015239460518</p>
        <p>malteoswitz@postfeld.de</p>
      </div>
      <div class="product-photo" role="img" aria-label="Foto eines Holzrings mit Metalleinlage auf einer Baumscheibe">
        <div class="brand-name">RINGHOLZ</div>
      </div>
      <div class="band-edge right"></div>
    </div>
    <address class="address">
      Lindgarbweg 9<br>83127 Altmühlried
    </address>
  </section>

  <section class="card card-front" role="img" aria-label="Vorderseite mit Foto bunter Holzperlen als Hintergrund">
    <div class="front-text front-title">Kugelwerk</div>
    <div class="front-text front-name">Malte Oswitz</div>
  </section>
</main>
</body>
</html>
```